Music Industry Business Needs a Business Card Design

Copper Lantern is an audio mastering company that has been in business for 20 years. Mastering is the final creative step in the music production chain. Our job is to make the music sound as good as it possibly can prior to release to the public. Our world is technical, artistic, precise. We work on everything from independent artists to the music for the Grandfield Cup. We are looking for a new, more modern business card design. I am uploading a copy of our logo, although it doesn't absolutely need to be included in the design.

Target Market(s)

Music Industry Professionals

Industry/Entity Type

Business

Contact Information for Business Card

Address, Phone, Email, Website, Name, Job Title

Font styles to use
Sans Serif

Requirements
Must have
• Sorry, but I don't have any concrete things to request. If I had a clear idea of what I want, I would probably just design something myself. I am looking for fresh input and thought I would try this.
Should not have
• Anything that is typical, such as headphones or the like.

```html
<!DOCTYPE html>
<html lang="en">
<head>
<meta charset="utf-8">
<title>Copper Lantern — Business Card</title>
<link rel="stylesheet" href="https://fonts.googleapis.com/css2?family=Lato:wght@300;400;700;900&display=swap">
<style>
  :root {
    --ink: #0a0a0a;
    --paper: #ffffff;
    --mark-tone-a: #161616;
    --mark-tone-b: #2a2a2a;
    --text: #111111;
  }
  html, body {
    margin: 0;
    padding: 0;
    overflow: hidden;
    background: var(--paper);
  }
  .card {
    position: relative;
    width: 1200px;
    height: 720px;
    background: var(--paper);
    overflow: hidden;
    font-family: "Lato", Arial, sans-serif;
    color: var(--text);
  }
  .brand-panel {
    position: absolute;
    left: 0;
    top: 0;
    width: 510px;
    height: 720px;
  }
  .brand-mark {
    position: absolute;
    left: 62px;
    top: 138px;
    width: 360px;
    height: 490px;
    background: linear-gradient(160deg, var(--mark-tone-b), var(--mark-tone-a));
  }
  .identity {
    position: absolute;
    left: 556px;
    top: 154px;
  }
  .identity__name {
    margin: 0;
    font-size: 34px;
    font-weight: 400;
    line-height: 1;
    letter-spacing: 0.3px;
  }
  .identity__name strong,
  .identity__role strong,
  .company__name strong {
    font-weight: 900;
  }
  .identity__role {
    margin: 12px 0 0;
    font-size: 23px;
    font-weight: 400;
    line-height: 1;
  }
  .company {
    position: absolute;
    left: 556px;
    top: 335px;
    width: 518px;
  }
  .company__name {
    margin: 0;
    padding-bottom: 10px;
    font-size: 41px;
    font-weight: 400;
    line-height: 1;
    border-bottom: 2px solid var(--ink);
  }
  .contact-list {
    list-style: none;
    margin: 6px 0 0;
    padding: 0;
  }
  .contact-list__item {
    display: flex;
    align-items: center;
    height: 42px;
    font-size: 20.5px;
    font-weight: 400;
  }
  .contact-list__icon {
    width: 22px;
    height: 22px;
    margin-right: 19px;
    flex: none;
    fill: var(--ink);
  }
</style>
</head>
<body>
<main class="card">
  <svg class="brand-panel" viewBox="0 0 510 720" aria-hidden="true">
    <rect x="0" y="0" width="486" height="720" fill="var(--ink)"/>
    <polygon points="486,159 508,190 486,221" fill="var(--ink)"/>
  </svg>
  <div class="brand-mark" role="img" aria-label="Copper Lantern brand mark with vertical name and flowing line"></div>

  <header class="identity">
    <h1 class="identity__name"><strong>YOUR</strong>&nbsp; FULL NAME</h1>
    <p class="identity__role"><strong>MUSIC</strong> DIRECTOR</p>
  </header>

  <section class="company">
    <h2 class="company__name"><strong>COPPER</strong>&nbsp; LANTERN</h2>
    <ul class="contact-list">
      <li class="contact-list__item">
        <svg class="contact-list__icon" viewBox="0 0 24 24" aria-hidden="true">
          <path d="M2 8c0-2 4-4 10-4s10 2 10 4v2h-5V8H7v2H2z"/>
          <path d="M7 11h10l3 8H4z"/>
          <circle cx="12" cy="15" r="2" fill="#fff"/>
        </svg>
        <span>+ 000 - 1234 - 5678</span>
      </li>
      <li class="contact-list__item">
        <svg class="contact-list__icon" viewBox="0 0 24 24" aria-hidden="true">
          <path d="M2 5h20v14H2z"/>
          <path d="M3 6l9 7 9-7" fill="none" stroke="#fff" stroke-width="1.6"/>
          <path d="M3 18l7-6M21 18l-7-6" fill="none" stroke="#fff" stroke-width="1.4"/>
        </svg>
        <span>yourmail@mail.com</span>
      </li>
      <li class="contact-list__item">
        <svg class="contact-list__icon" viewBox="0 0 24 24" aria-hidden="true">
          <g fill="none" stroke="var(--ink)" stroke-width="2.2" stroke-linecap="round">
            <path d="M10 14a4 4 0 0 0 5.6 0l3.5-3.5a4 4 0 0 0-5.6-5.6l-1.5 1.5"/>
            <path d="M14 10a4 4 0 0 0-5.6 0l-3.5 3.5a4 4 0 0 0 5.6 5.6l1.5-1.5"/>
          </g>
        </svg>
        <span>www.copperlantern.com</span>
      </li>
      <li class="contact-list__item">
        <svg class="contact-list__icon" viewBox="0 0 24 24" aria-hidden="true">
          <path d="M12 3L1 12h3v9h6v-6h4v6h6v-9h3z"/>
        </svg>
        <span>Copperlantern, copperlantern Road, 54321</span>
      </li>
    </ul>
  </section>
</main>
</body>
</html>
```